Tri-fold Brochure Design for Banking Business

The brochure we have needs to be improved - more business like and more attractive. Logo file and brochure is attached. I would like to be able to edit the text after you get done. Your ideas and changes to text are welcome. See our website www.korvanbridgegrp.com for our theme. We can use indesign to edit the text after you complete. However, please make changes to the text we have in the design that it uploaded. Your comments and changes are welcome.

Target Market(s)

Human Resources and learning & development staff at the global investment banks - Pellham Trask, QWNR, etc.

Industry/Entity Type

Investment Banking

Logo Text

Korvan Bridge Group

Font styles to use
Serif
Sans Serif

Colors
33a6d7
0493ce
3277b5
fbf289
fdf9cf
fbee3e
0555a3
85acd3

Requirements
Must have
• Must be similar to our website www.korvanbridgegrp.com. Needs to be business-like, clean fonts, sharp design. Our logo - of course.
Nice to have
• City images - seems to be our theme.

```html
<!DOCTYPE html>
<html lang="en">
<head>
<meta charset="utf-8">
<title>Korvan Bridge Group – Tri-fold Brochure</title>
<link rel="stylesheet" href="https://fonts.googleapis.com/css2?family=Lato:wght@400;700&family=Montserrat:wght@300;400;600;800;900&display=swap">
<style>
  :root{
    --stage:#235b6d;
    --royal:#0d3fd6;
    --royal-deep:#0a2fa8;
    --navy:#0a1e8c;
    --yellow:#fbee3e;
    --white:#ffffff;
    --ink:#1b1b1b;
    --sky-top:#9fc4e4;
    --sky-low:#3d6a9a;
    --map:#0c3f9a;
  }
  *{box-sizing:border-box;margin:0;padding:0}
  html,body{width:1200px;height:1021px;overflow:hidden}
  body{background:var(--stage);font-family:"Lato",sans-serif;position:relative}
  .brochure{position:absolute;left:45px;top:80px;width:1110px;height:860px;display:flex;box-shadow:0 20px 50px rgba(0,0,0,.35)}
  .panel{position:relative;width:370px;height:860px;overflow:hidden;background:var(--white)}
  .panel-art{position:absolute;inset:0;width:370px;height:860px}
  .panel-content{position:absolute;inset:0}

  /* About panel */
  .about-title{position:absolute;left:36px;top:568px;font-family:"Montserrat",sans-serif;font-weight:900;font-size:24px;letter-spacing:1px;color:var(--white)}
  .about-text{position:absolute;left:36px;top:612px;width:300px;font-size:14px;line-height:1.45;color:var(--white)}
  .site{position:absolute;right:30px;bottom:30px;font-size:15px;color:var(--white);letter-spacing:.3px;white-space:nowrap}

  /* Contact panel */
  .brand{display:flex;align-items:center;gap:10px;font-family:"Montserrat",sans-serif;font-weight:600;color:var(--ink);letter-spacing:2px;white-space:nowrap}
  .brand-dot{width:14px;height:14px;border-radius:50%;background:var(--royal);flex:none}
  .contact-brand{position:absolute;left:0;right:0;top:330px;justify-content:center;font-size:15px}
  .contact-list{position:absolute;left:0;right:0;top:378px;list-style:none;text-align:center;color:var(--ink);font-size:13.5px;line-height:1.35}
  .contact-list li{margin-bottom:12px}
  .contact-list svg{display:block;margin:0 auto 4px}
  .map{position:absolute;left:80px;top:592px;width:210px;height:86px;border-radius:50%;background:radial-gradient(ellipse at center,var(--map) 0%,var(--map) 60%,rgba(12,63,154,0) 72%)}

  /* Cover panel */
  .cover-brand{position:absolute;left:30px;top:64px;font-size:18px;letter-spacing:2px}
  .cover-brand .brand-dot{width:16px;height:16px}
  .tagline{position:absolute;right:28px;top:600px;text-align:right;font-family:"Montserrat",sans-serif;color:var(--white);font-size:23px;line-height:1.2;font-weight:300}
  .tagline strong{font-weight:900}
</style>
</head>
<body>
<main class="brochure">

  <!-- Panel 1: About -->
  <section class="panel panel-about">
    <svg class="panel-art" viewBox="0 0 370 860">
      <defs>
        <linearGradient id="aboutSky" x1="0" y1="0" x2="0" y2="1">
          <stop offset="0" stop-color="#cfe3f2"/><stop offset=".6" stop-color="#7f98a8"/><stop offset="1" stop-color="#3f5560"/>
        </linearGradient>
        <linearGradient id="blueBand" x1="0" y1="0" x2="0" y2="1">
          <stop offset="0" stop-color="#1246e6"/><stop offset="1" stop-color="#0a2fb0"/>
        </linearGradient>
      </defs>
      <g role="img" aria-label="City skyline photograph with a glass tower and riverside buildings">
        <rect width="370" height="600" fill="url(#aboutSky)"/>
      </g>
      <path d="M0 540 Q200 490 370 240 L370 860 L0 860 Z" fill="url(#blueBand)"/>
      <path d="M0 540 Q200 490 370 240" fill="none" stroke="var(--yellow)" stroke-width="7"/>
    </svg>
    <div class="panel-content">
      <h2 class="about-title">ABOUT US</h2>
      <p class="about-text">Korvan Bridge Group efficiently provides complete sales, marketing and logistical support for all our programs, no matter the location. Our globally located trainers have extensive experience, both as industry professionals and as trainers. Our highly qualified logistical team complement the training services, providing reliable and efficient support.</p>
      <p class="site">www.korvanbridgegrp.com</p>
    </div>
  </section>

  <!-- Panel 2: Contact -->
  <section class="panel panel-contact">
    <svg class="panel-art" viewBox="0 0 370 860">
      <defs>
        <linearGradient id="contactSky" x1="0" y1="0" x2="0" y2="1">
          <stop offset="0" stop-color="#8fc0ea"/><stop offset=".7" stop-color="#5a5a60"/><stop offset="1" stop-color="#2f5f86"/>
        </linearGradient>
        <linearGradient id="blueBand2" x1="0" y1="0" x2="0" y2="1">
          <stop offset="0" stop-color="#1246e6"/><stop offset="1" stop-color="#0a2fb0"/>
        </linearGradient>
      </defs>
      <g role="img" aria-label="Photograph of a waterfront city skyline with skyscrapers">
        <path d="M0 0 H370 V110 Q250 290 0 300 Z" fill="url(#contactSky)"/>
      </g>
      <path d="M0 300 Q250 290 370 110" fill="none" stroke="var(--navy)" stroke-width="8"/>
      <path d="M0 300 Q250 290 370 110" fill="none" stroke="var(--yellow)" stroke-width="3" transform="translate(0,-6)"/>
      <path d="M0 770 Q260 760 370 640 L370 860 L0 860 Z" fill="url(#blueBand2)"/>
      <path d="M0 770 Q260 760 370 640" fill="none" stroke="var(--yellow)" stroke-width="7"/>
    </svg>
    <div class="panel-content">
      <div class="brand contact-brand"><span class="brand-dot"></span>KORVAN BRIDGE GROUP</div>
      <ul class="contact-list">
        <li>
          <svg width="16" height="20" viewBox="0 0 16 20"><path d="M8 1a6 6 0 0 0-6 6c0 5 6 12 6 12s6-7 6-12a6 6 0 0 0-6-6z" fill="none" stroke="var(--royal)" stroke-width="1.6"/><circle cx="8" cy="7" r="2" fill="var(--royal)"/></svg>
          Unit 7B Harlow Trade Centre<br>212-218 Marsden Rd. East Quay
        </li>
        <li>
          <svg width="16" height="16" viewBox="0 0 16 16"><path d="M3 1l3 3-2 2c1 2 3 4 5 5l2-2 3 3-2 2C7 14 2 9 1 3z" fill="var(--royal)"/></svg>
          852 3180 5562
        </li>
        <li>
          <svg width="18" height="13" viewBox="0 0 18 13"><rect x="1" y="1" width="16" height="11" fill="none" stroke="var(--royal)" stroke-width="1.4"/><path d="M1 1l8 6 8-6" fill="none" stroke="var(--royal)" stroke-width="1.4"/></svg>
          info@korvanbridgegrp.com
        </li>
        <li>
          <svg width="16" height="16" viewBox="0 0 16 16"><circle cx="8" cy="8" r="7" fill="none" stroke="var(--royal)" stroke-width="1.4"/><ellipse cx="8" cy="8" rx="3" ry="7" fill="none" stroke="var(--royal)" stroke-width="1.2"/><path d="M1 8h14" stroke="var(--royal)" stroke-width="1.2"/></svg>
          www.korvanbridgegrp.com
        </li>
      </ul>
      <div class="map" role="img" aria-label="World map silhouette"></div>
      <p class="site">www.korvanbridgegrp.com</p>
    </div>
  </section>

  <!-- Panel 3: Cover -->
  <section class="panel panel-cover">
    <svg class="panel-art" viewBox="0 0 370 860">
      <defs>
        <linearGradient id="coverSky" x1="0" y1="0" x2="0" y2="1">
          <stop offset="0" stop-color="var(--sky-top)"/><stop offset=".55" stop-color="#577ea6"/><stop offset="1" stop-color="var(--sky-low)"/>
        </linearGradient>
        <linearGradient id="coverBlue" x1="0" y1="0" x2="0" y2="1">
          <stop offset="0" stop-color="#0d3fd6" stop-opacity=".85"/><stop offset="1" stop-color="#0a2fa8"/>
        </linearGradient>
      </defs>
      <g role="img" aria-label="Evening harbour skyline photograph with a tall office tower">
        <rect width="370" height="860" fill="url(#coverSky)"/>
      </g>
      <path d="M0 0 H370 V90 L170 205 L0 130 Z" fill="var(--white)"/>
      <path d="M0 130 L170 205 L370 90" fill="none" stroke="var(--navy)" stroke-width="6"/>
      <path d="M0 520 Q220 440 370 260 L370 860 L0 860 Z" fill="url(#coverBlue)"/>
      <path d="M0 520 Q220 440 370 260" fill="none" stroke="var(--yellow)" stroke-width="7"/>
    </svg>
    <div class="panel-content">
      <div class="brand cover-brand"><span class="brand-dot"></span>KORVAN BRIDGE GROUP</div>
      <p class="tagline">YOUR EXPERT TRAINING<br>AND <strong>CONSULTING</strong><br>PARTNER</p>
    </div>
  </section>

</main>
</body>
</html>
```